Brand new letterhead, business card, email signature etc.

We are a financial company in London, UK. Our website is www.marlowvane.com. We're wanting a complete remodel of the company colours, letter head, business cards, email signatures, etc. Looking to keep the same font for the company name. I have upload a colour palette that we want to work with. We're looking for company letterhead for outgoing letters/ correspondence, letterhead for internal documentation, email signatures, e-letters. etc. Ultimately we will redesign the entire website also. It is important that our clients get a strong, secure, warm, trustworthy, solid feeling and first impression.
Updates

Designs look the same

Target Market(s)

Institutional investors, (ultra) high net worth individuals

Industry/Entity Type

Finance, Invesments banking.

Font styles to use
Other font styles liked:
• Current font is "Champagne & Limousines"

Requirements
Must have
• Must use the colours provided on the PDF uploaded to the portal. The purple = main colour. The red = accent colour.
Nice to have
• Nice to use same font as now for the company name "Quillmoor". Font is "Champagne & Limousines". Nice to have some reference to the old logo flower, but only subtle.
Should not have
• Do not use the colour red from our website. Use the colours provided on the colour palette PDF that I uploaded in the portal.

```html
<!DOCTYPE html>
<html lang="en">
<head>
<meta charset="utf-8">
<title>Quillmoor — Business Card</title>
<link rel="stylesheet" href="https://fonts.googleapis.com/css2?family=Josefin+Sans:wght@300&family=Questrial&display=swap">
<style>
  :root {
    --bg: #2c2c2c;
    --card: #ffffff;
    --card-shade: #ececec;
    --plum: #2e0b1c;
    --accent: #d9341c;
    --ink: #2a1a20;
  }
  * { margin: 0; padding: 0; box-sizing: border-box; }
  html, body { width: 1200px; height: 900px; overflow: hidden; background: var(--bg); }
  .canvas {
    width: 1200px; height: 900px;
    display: flex; flex-direction: column; align-items: center; justify-content: center; gap: 40px;
  }
  .card {
    position: relative; width: 700px; height: 400px;
    background: linear-gradient(135deg, var(--card) 40%, var(--card-shade) 100%);
    color: var(--ink);
    font-family: "Questrial", sans-serif;
  }
  .wordmark {
    position: absolute;
    font-family: "Josefin Sans", sans-serif; font-weight: 300;
    text-transform: uppercase; color: var(--ink);
  }
  .card--front .wordmark { top: 42px; right: 45px; font-size: 34px; letter-spacing: 7px; }
  .card--back .wordmark { bottom: 70px; right: 60px; font-size: 46px; letter-spacing: 9px; }
  .band-plum { position: absolute; left: 0; top: 0; bottom: 0; width: 56px; background: var(--plum); }
  .band-accent { position: absolute; left: 56px; top: 0; bottom: 0; width: 12px; background: var(--accent); }
  .holder { position: absolute; left: 118px; top: 168px; }
  .holder-name {
    font-family: "Josefin Sans", sans-serif; font-weight: 300;
    font-size: 24px; letter-spacing: 4px; text-transform: uppercase;
  }
  .holder-role { color: var(--accent); font-size: 15px; margin-top: 2px; }
  .contacts { position: absolute; left: 118px; top: 238px; list-style: none; font-size: 16px; }
  .contacts li { display: flex; align-items: center; gap: 10px; height: 22px; }
  .contacts svg { width: 13px; height: 13px; fill: var(--accent); flex: none; }
  .contacts .web { color: var(--accent); }
  .address {
    position: absolute; right: 45px; top: 178px;
    font-style: normal; text-align: right; font-size: 15px; line-height: 19px;
  }
</style>
</head>
<body>
<main class="canvas">
  <section class="card card--front">
    <div class="band-plum"></div>
    <div class="band-accent"></div>
    <div class="wordmark">Quillmoor</div>
    <div class="holder">
      <div class="holder-name">Edwin Calder</div>
      <div class="holder-role">chairman</div>
    </div>
    <ul class="contacts">
      <li>
        <svg viewBox="0 0 16 16" aria-hidden="true"><path d="M1 6c0-2 3-4 7-4s7 2 7 4v1.5h-3.5V5.5h-7V7.5H1z"/><path d="M4 8.5 6 6.5h4l2 2v5.5H4z"/></svg>
        <span>+4470 5512 3098</span>
      </li>
      <li>
        <svg viewBox="0 0 16 16" aria-hidden="true"><path d="M1 4h14v1L8 9.5 1 5z"/><path d="M1 6.5 8 11l7-4.5V13H1z"/></svg>
        <span>e@marlowvane.com</span>
      </li>
      <li>
        <svg viewBox="0 0 16 16" aria-hidden="true"><path fill-rule="evenodd" d="M8 1a7 7 0 1 1 0 14A7 7 0 0 1 8 1zm-1 1.6A5.5 5.5 0 0 0 2.6 7.2h2.6c.1-1.8.7-3.4 1.8-4.6zm2 0c1.1 1.2 1.7 2.8 1.8 4.6h2.6A5.5 5.5 0 0 0 9 2.6zM6.7 7.2h2.6C9.2 5.6 8.7 4.2 8 3.3 7.3 4.2 6.8 5.6 6.7 7.2zm0 1.6c.1 1.6.6 3 1.3 3.9.7-.9 1.2-2.3 1.3-3.9zm-4.1 0A5.5 5.5 0 0 0 7 13.4c-1.1-1.2-1.7-2.8-1.8-4.6zm8.2 0c-.1 1.8-.7 3.4-1.8 4.6a5.5 5.5 0 0 0 4.4-4.6z"/></svg>
        <span class="web">www.marlowvane.com</span>
      </li>
    </ul>
    <address class="address">
      12 Harrow Lane<br>
      EC3N 2PL, London<br>
      United Kingdom
    </address>
  </section>

  <section class="card card--back">
    <div class="wordmark">Quillmoor</div>
  </section>
</main>
</body>
</html>
```